Plucky Pip Color In Book

The following text must apply;

PLUCKY PIP COLOUR IN BOOK
This new Plucky Pip colour in book will support and educate your Boorais being DEADLY during the pandemic. This also comes with the Plucky Pip Kit which includes;
"Plucky Pip on the Ferry" Reading book
Gumnut Kids Keep Lungs Clear Car Sticker
Gumnut Kids Keep Lungs Clear Keyring
Gumnut Kids Keep Lungs Clear Car Freshener

Register online to get your free Plucky Pip Kit

Free delivery

Target Market(s)

Children and Families

Requirements
Nice to have
• Fun themed.

```html
<!DOCTYPE html>
<html lang="en">
<head>
<meta charset="utf-8">
<title>Plucky Pip Colour In Book</title>
<link href="https://fonts.googleapis.com/css2?family=Bangers&family=Arimo:wght@400;700&display=swap" rel="stylesheet">
<style>
  :root{
    --page:#ececec;
    --sky:#1fa6ea;
    --sky-light:#6fd0ff;
    --sky-deep:#0a86d0;
    --yellow:#ffd400;
    --red:#e0281c;
    --ink:#111111;
    --white:#ffffff;
    --kraft:#d8c8a6;
    --kraft-dark:#c9b792;
    --book-grey:#5b5b5b;
    --book-cream:#e9e6dc;
  }
  *{box-sizing:border-box;margin:0;padding:0}
  html,body{width:1200px;height:1000px;overflow:hidden;background:var(--page)}
  .canvas{position:relative;width:1200px;height:1000px}
  .poster{position:absolute;left:270px;top:30px;width:657px;height:932px;overflow:hidden;
    background:radial-gradient(ellipse at 50% 40%,var(--sky-light) 0%,var(--sky) 45%,var(--sky-deep) 100%)}
  .abs{position:absolute}
  .display{font-family:"Bangers",system-ui,sans-serif;letter-spacing:1px}

  .title{left:0;width:657px;top:42px;text-align:center;font-size:118px;line-height:1;color:var(--yellow);
    transform:rotate(-3deg);-webkit-text-stroke:2px var(--ink);
    text-shadow:6px 6px 0 var(--red),8px 8px 0 var(--ink)}
  .subtitle{left:355px;top:146px;font-size:38px;color:var(--yellow);transform:rotate(-3deg);
    -webkit-text-stroke:1.5px var(--ink);text-shadow:3px 3px 0 var(--ink)}

  .delivery-badge{left:95px;top:215px;width:122px;height:122px;border-radius:50%;background:var(--yellow);
    border:3px solid var(--ink);display:flex;align-items:center;justify-content:center;text-align:center;
    font-family:"Arimo",Arial,sans-serif;font-size:17px;line-height:1.4;color:var(--ink);padding-right:18px}

  .colour-book{left:208px;top:198px;width:262px;height:372px;background:var(--book-grey);
    box-shadow:6px 8px 14px rgba(0,0,0,.45);border-radius:2px 6px 6px 2px}
  .colour-book .book-title{left:0;width:100%;top:28px;text-align:center;font-size:62px;color:var(--yellow);
    -webkit-text-stroke:1.5px var(--ink);text-shadow:3px 3px 0 var(--red)}
  .colour-book .hero-art{left:60px;top:92px;width:150px;height:260px;border-radius:40px 40px 6px 6px;
    background:linear-gradient(180deg,#d8402a 0%,#c8321f 60%,#7a5a44 100%)}
  .colour-book .book-sub{left:0;width:100%;top:208px;text-align:center;font-size:32px;color:var(--yellow);
    -webkit-text-stroke:1px #7a5a10}
  .colour-book .sticker-art{left:172px;top:272px;width:82px;height:64px;border-radius:10px;
    background:linear-gradient(135deg,var(--yellow),#f0a800 60%,var(--red))}

  .reading-book{left:46px;top:312px;width:200px;height:275px;background:var(--book-cream);
    box-shadow:5px 7px 12px rgba(0,0,0,.45);border-radius:2px 4px 4px 2px;overflow:hidden}
  .reading-book .rb-title{left:10px;top:18px;font-family:"Arimo",Arial,sans-serif;font-size:19px;font-weight:700;color:var(--red)}
  .reading-book .rb-sub{left:10px;top:42px;font-family:"Arimo",Arial,sans-serif;font-size:13px;color:#333}
  .reading-book .scene-art{left:0;top:66px;width:200px;height:209px;
    background:linear-gradient(180deg,#aab58a 0%,#c9c2a2 40%,#8a6a5a 70%,#b8b8b0 100%)}

  .merch{border-radius:14px}
  .merch-sticker{left:432px;top:300px;width:120px;height:88px;background:linear-gradient(135deg,var(--red),var(--yellow) 55%,var(--ink) 120%);transform:rotate(-6deg)}
  .merch-fresh-a{left:538px;top:454px;width:104px;height:74px;background:linear-gradient(135deg,var(--yellow),var(--red) 110%);transform:rotate(-8deg)}
  .merch-fresh-b{left:488px;top:512px;width:100px;height:74px;background:linear-gradient(135deg,var(--yellow),var(--red) 110%);transform:rotate(-8deg)}
  .merch-keyring{left:478px;top:434px;width:62px;height:56px;border-radius:6px;background:linear-gradient(135deg,var(--white),#ddd);transform:rotate(-12deg)}
  .cords{left:0;top:0}

  .paper{left:0;top:580px;width:657px;height:352px}

  .pitch{left:0;width:657px;top:598px;text-align:center;font-size:24px;line-height:30px;color:var(--white);
    font-style:italic;-webkit-text-stroke:1px var(--ink);text-shadow:2px 2px 0 var(--ink),-1px -1px 0 var(--ink)}
  .pitch .hl{color:var(--yellow)}
  .kit-list{left:0;width:657px;top:715px;text-align:center;list-style:none;
    font-family:"Arimo",Arial,sans-serif;font-size:15.5px;line-height:16px;color:var(--ink)}

  .cta{display:flex;align-items:center;justify-content:center;border:3px solid var(--ink);
    box-shadow:5px 5px 0 var(--ink);font-size:26px;color:var(--ink);transform:skewX(-6deg)}
  .cta-register{left:160px;top:792px;width:222px;height:54px;background:var(--yellow)}
  .cta-kit{left:302px;top:838px;width:226px;height:60px;background:var(--red);color:var(--yellow);font-size:24px}
  .cta-link{left:395px;top:808px;font-size:20px;color:var(--ink);font-style:italic}

  .org{left:18px;top:850px;width:110px;display:flex;flex-direction:column;align-items:center;gap:8px;
    font-family:"Arimo",Arial,sans-serif;font-size:10px;font-weight:700;color:var(--ink);text-align:center;line-height:1.2}
  .org-mark{width:34px;height:34px;background:var(--red)}
</style>
</head>
<body>
<div class="canvas">
  <main class="poster">
    <h1 class="abs display title">PLUCKY PIP</h1>
    <p class="abs display subtitle">COLOUR IN BOOK</p>

    <div class="abs delivery-badge">FREE<br>DELIVERY!</div>

    <div class="abs colour-book">
      <div class="abs hero-art" role="img" aria-label="Illustrated superhero character on the colour in book cover"></div>
      <p class="abs display book-title">PLUCKY PIP</p>
      <p class="abs display book-sub">Colour In Book</p>
      <div class="abs sticker-art" role="img" aria-label="Gumnut Kids Keep Lungs Clear campaign lettering"></div>
    </div>

    <div class="abs reading-book">
      <p class="abs rb-title">Plucky Pip</p>
      <p class="abs rb-sub">On The Ferry</p>
      <div class="abs scene-art" role="img" aria-label="Illustrated family walking beside a colourful mural"></div>
    </div>

    <svg class="abs cords" width="657" height="600" aria-hidden="true">
      <path d="M552 218 C 535 260, 520 330, 530 438" stroke="var(--ink)" stroke-width="1.5" fill="none"/>
      <circle cx="518" cy="428" r="7" stroke="#999" stroke-width="2" fill="none"/>
    </svg>
    <div class="abs merch merch-sticker" role="img" aria-label="Gumnut Kids Keep Lungs Clear car sticker"></div>
    <div class="abs merch-keyring" role="img" aria-label="Gumnut Kids Keep Lungs Clear keyring"></div>
    <div class="abs merch merch-fresh-a" role="img" aria-label="Gumnut Kids Keep Lungs Clear car freshener"></div>
    <div class="abs merch merch-fresh-b" role="img" aria-label="Gumnut Kids Keep Lungs Clear car freshener"></div>

    <svg class="abs paper" viewBox="0 0 657 352" preserveAspectRatio="none" aria-hidden="true">
      <path d="M0 60 L40 52 L80 62 L130 50 L190 58 L240 46 L300 55 L360 44 L420 52 L480 40 L540 50 L600 30 L657 8 L657 352 L0 352 Z" fill="var(--white)"/>
      <path d="M0 66 L40 58 L80 68 L130 56 L190 64 L240 52 L300 61 L360 50 L420 58 L480 46 L540 56 L600 36 L657 14 L657 352 L0 352 Z" fill="var(--kraft)"/>
    </svg>

    <p class="abs display pitch">
      This new <span class="hl">Plucky Pip colour in book</span> will support<br>
      and educate your Boorais being DEADLY during the pandemic.<br>
      <span class="hl">The Plucky Pip Kit includes;</span>
    </p>

    <ul class="abs kit-list">
      <li>"Plucky Pip on the Ferry" Reading book</li>
      <li>Gumnut Kids Keep Lungs Clear Car Sticker</li>
      <li>Gumnut Kids Keep Lungs Clear Keyring</li>
      <li>Gumnut Kids Keep Lungs Clear Car Freshener</li>
    </ul>

    <div class="abs display cta cta-register">REGISTER ONLINE</div>
    <p class="abs display cta-link">TO GET YOUR</p>
    <div class="abs display cta cta-kit">FREE PLUCKY PIP KIT</div>

    <div class="abs org">
      <span class="org-mark"></span>
      <span>RIVERBEND COMMUNITY HEALTH</span>
    </div>
  </main>
</div>
</body>
</html>
```